Talvor GmbH business card

We Talvor GmbH based in Switzerland are looking for a business card design. The Fresh Jung, appealing to customers of all kinds. We already have a logo to upload but still a business card. Details: Talvor GmbH Address: Lindenweg 14b in 9476 Brugwil. Tel: 41 79 462 37 18, web: Talvor.ch, E-mail: info@Talvor.ch Facebook: Talvor GmbH I am the Managing Director: Luka Petrovac. On reverse: Title: Transporter and bus rental Gross: Without deposit Super prices
Contact Information for Business Card
Siehe Projektbeschreibung
Requirements
Should not have
- Other pictures

```html
<!DOCTYPE html>
<html lang="de">
<head>
<meta charset="utf-8">
<title>Talvor GmbH – Visitenkarte</title>
<link rel="stylesheet" href="https://fonts.googleapis.com/css2?family=Montserrat:wght@400;500;600;700&family=Quicksand:wght@400;500&display=swap">
<style>
  :root{
    --stage:#0d0d0d;
    --paper:#ffffff;
    --blue:#4f6a9c;
    --blue-deep:#2f3d85;
    --blue-light:#7a8fb8;
    --navy:#2a2a6e;
    --text-light:#ffffff;
    --muted:#c9d3e6;
  }
  *{margin:0;padding:0;box-sizing:border-box}
  html,body{width:1200px;height:900px;overflow:hidden;background:var(--stage)}
  .stage{position:relative;width:1200px;height:900px;background:var(--stage)}
  .card{position:absolute;left:393px;width:403px;height:265px;overflow:hidden;background:var(--paper)}
  .card--front{top:173px}
  .card--back{top:475px}
  .card svg.shapes{position:absolute;inset:0}
  .brand{position:absolute;display:flex;align-items:center;gap:8px;font-family:'Montserrat',sans-serif;font-weight:700;color:var(--navy)}
  .brand__mark{background:var(--navy)}
  .front-brand{left:22px;top:166px;font-size:26px;letter-spacing:.5px}
  .front-brand .brand__mark{width:18px;height:18px}
  .front-tagline{position:absolute;left:89px;top:206px;font-family:'Quicksand',sans-serif;font-size:10.5px;color:var(--blue-deep)}
  .front-claims{position:absolute;left:114px;top:221px;font-family:'Quicksand',sans-serif;font-size:8.5px;color:var(--blue-deep)}
  .front-watermark{position:absolute;left:262px;top:80px;font-family:'Montserrat',sans-serif;font-weight:700;font-size:30px;color:rgba(255,255,255,.8)}
  .back-brand{left:26px;top:102px;font-size:30px}
  .back-brand .brand__mark{width:22px;height:22px}
  .person{position:absolute;left:247px;top:89px;font-family:'Montserrat',sans-serif}
  .person__name{font-size:13px;font-weight:700;color:var(--text-light)}
  .person__name span{color:var(--navy)}
  .person__role{display:flex;align-items:flex-end;margin-top:0;font-family:'Quicksand',sans-serif;font-size:7.5px;color:var(--muted);width:156px}
  .person__role i{flex:1;height:1px;background:var(--muted);margin-left:2px;margin-bottom:1px}
  .contacts{position:absolute;left:208px;top:159px;list-style:none;font-family:'Quicksand',sans-serif;font-size:9.5px;color:var(--text-light);line-height:12.8px}
  .contacts li{display:flex;align-items:flex-start}
  .contacts svg{width:7px;height:7px;margin:3px 11px 0 2px;fill:var(--text-light);flex:none}
  .contacts .no-icon{width:7px;margin-right:13px;flex:none}
</style>
</head>
<body>
<main class="stage">

  <section class="card card--front" aria-label="Vorderseite">
    <svg class="shapes" width="403" height="265" viewBox="0 0 403 265">
      <defs>
        <linearGradient id="frontBlue" x1="0" y1="0" x2="0.4" y2="1">
          <stop offset="0" stop-color="#7f93b9"/>
          <stop offset="1" stop-color="#2e3c87"/>
        </linearGradient>
      </defs>
      <polygon points="237,142 300,265 288,265 233,148" fill="#4d63a8"/>
      <polygon points="317,0 403,0 403,265 292,265 211,55" fill="url(#frontBlue)"/>
    </svg>
    <div class="front-watermark">Talvor</div>
    <div class="brand front-brand"><span class="brand__mark"></span>Talvor GmbH</div>
    <p class="front-tagline">Transporter und Bus Vermietung</p>
    <p class="front-claims">Ohne Kaution &nbsp;|&nbsp; Super Preise</p>
  </section>

  <section class="card card--back" aria-label="Rückseite">
    <svg class="shapes" width="403" height="265" viewBox="0 0 403 265">
      <rect width="403" height="265" fill="var(--blue)"/>
      <polygon points="172,145 145,265 124,265" fill="#2a2a6e"/>
      <polygon points="0,0 82,0 204,62 144,265 0,265" fill="var(--paper)"/>
    </svg>
    <div class="brand back-brand"><span class="brand__mark"></span>Talvor</div>

    <div class="person">
      <p class="person__name">Luka <span>Petrovac</span></p>
      <p class="person__role">Geschäftsführer<i></i></p>
    </div>

    <ul class="contacts">
      <li><svg viewBox="0 0 10 10"><path d="M2 0l2 2-1 1.5q1 2 3.5 3.5L8 6l2 2-1.5 2Q4 9.5 0 1.5z"/></svg>+41 79 462 37 18</li>
      <li><svg viewBox="0 0 10 10"><path d="M0 2h10v6H0z M0 2l5 3 5-3" fill="none" stroke="#fff" stroke-width="1.5"/></svg>info@Talvor.ch</li>
      <li><svg viewBox="0 0 10 10"><path d="M5 0l5 5H8.5v5h-7V5H0z"/></svg>Talvor.ch</li>
      <li><svg viewBox="0 0 10 10"><rect width="10" height="10"/></svg>Talvor GmbH</li>
      <li><svg viewBox="0 0 10 10"><path d="M5 0a3.5 3.5 0 0 1 3.5 3.5C8.5 6 5 10 5 10S1.5 6 1.5 3.5A3.5 3.5 0 0 1 5 0z"/></svg>Lindenweg 14b</li>
      <li><span class="no-icon"></span>9476 Brugwil</li>
    </ul>
  </section>

</main>
</body>
</html>
```